New Shopify design for existing webshop

We have an existing webshop on an old Magento solution. Now we're going to switch to Shopify. We need a new Shopify theme for this.

Our old website is www.tessin-brand.ch

We have the product categories:
Postage stamps
Tobler albums & accessories
Coins and banknotes
Franking service

In addition, we need the pages to be prominently integrated similar to the products:
Missing list service
Purchases

We can include the following pages at the bottom, less prominently on the page:
Contact
imprint
Conditions
revocation
data protection

shipping
Guarantee of trust

The products should be in the foreground on the website. Our logo can be incorporated. We also upload some images that can be used for the design. Of course you don't have to.

The new design does not have to be based on the old design. It can be something completely new. All pictures that we have on the website can of course also be used. But I also added some pictures to the project that fit our company.

Our company:
The company, which was founded by Paul Tobler in 1931, has developed into one of the largest and best-known Swiss postage stamp houses over the past 98 years.

Target Market(s)

Germany, Switzerland

Font styles to use
Serif
Sans Serif

Requirements
Must have
• The products stamps that you can buy should be in the foreground.
If images are used in the design, please focus on Swiss stamps and coins (no foreign coins or stamps)

```html
<!DOCTYPE html>
<html lang="de">
<head>
<meta charset="utf-8">
<title>Marken Tobler</title>
<link href="https://fonts.googleapis.com/css2?family=Bebas+Neue&family=Open+Sans:wght@300;400;600;700;800&display=swap" rel="stylesheet">
<style>
:root{
  --blue:#2e3192;
  --red:#ed1c24;
  --grey-bg:#e6e6e6;
  --text:#4d4d4d;
  --nav-grey:#9a9a9a;
  --black:#000;
  --white:#fff;
  --label:"Bebas Neue", sans-serif;
  --body:"Open Sans", sans-serif;
}
*{margin:0;padding:0;box-sizing:border-box}
html,body{width:1200px;height:2526px;overflow:hidden}
body{position:relative;background:var(--white);font-family:var(--body);color:var(--text)}
.abs{position:absolute}
a{color:inherit;text-decoration:none}

/* header */
.site-header{left:0;top:0;width:1200px;height:73px;background:var(--white)}
.brand{left:130px;top:18px;font-family:var(--body);font-weight:800;font-size:28px;color:var(--blue);letter-spacing:1px;display:flex;align-items:center;gap:10px}
.brand-dot{width:22px;height:22px;background:var(--red);border-radius:50%}
.account-nav{left:478px;top:30px;display:flex;gap:13px;font-family:var(--label);font-size:17px;color:var(--nav-grey);letter-spacing:.5px}
.account-nav .active{color:var(--blue)}
.nav-caret{left:481px;top:66px;width:0;height:0;border-left:14px solid transparent;border-right:14px solid transparent;border-bottom:8px solid var(--blue)}

/* hero */
.hero{left:0;top:73px;width:1200px;height:476px;background:var(--blue);overflow:hidden}
.category-nav{left:135px;top:5px;display:flex;align-items:center;font-family:var(--label);font-size:18px;color:var(--white);letter-spacing:.5px}
.category-nav a{padding:0 26px;line-height:39px}
.category-nav .current{background:var(--red);border-radius:4px;padding:0 20px}
.coin-decor{left:135px;top:155px;width:510px;height:260px;border-radius:130px;background:radial-gradient(ellipse at 80% 50%,rgba(130,140,220,.55),rgba(30,30,90,.5) 60%,rgba(46,49,146,0) 100%)}
.stamp-art{left:667px;top:40px;width:419px;height:436px;background:radial-gradient(circle at 50% 45%,#e3c9cf 0%,#c9606a 30%,#7f9fcf 55%,#2c4f8a 82%,#10182a 100%);border:6px solid #111}
.hero-title{left:143px;top:112px;font-weight:800;font-size:56px;line-height:56px;color:var(--white)}
.hero-sub{left:145px;top:222px;font-weight:300;font-size:33px;color:var(--white)}
.hero-copy{left:148px;top:273px;width:325px;font-size:16.5px;line-height:23px;color:var(--white)}
.btn{background:var(--red);color:var(--white);font-family:var(--label);border-radius:4px;text-align:center}
.shop-now{left:148px;top:371px;width:124px;height:39px;line-height:41px;font-size:22px;letter-spacing:.5px}

/* section divider */
.divider-line{left:311px;width:574px;height:6px;background:var(--red)}
.divider-pill{height:38px;line-height:40px;background:var(--red);color:var(--white);font-family:var(--label);font-size:23px;border-radius:10px;text-align:center;letter-spacing:.5px}

.welcome{left:235px;top:627px;width:730px;text-align:center;font-size:18px;line-height:22px;color:var(--text)}

/* products */
.products{left:0;top:826px;width:1200px;height:1350px;background:var(--grey-bg)}
.product{width:267px;height:372px}
.product-image{left:0;top:0;width:267px;height:266px;background:var(--white)}
.coin{left:28px;top:20px;width:222px;height:222px;border-radius:50%;background:radial-gradient(circle at 40% 35%,#f7e7a6 0%,#dbb25a 55%,#a97a2a 100%)}
.product-name{left:0;top:281px;font-family:var(--label);font-size:24px;color:var(--blue);letter-spacing:.5px}
.product-price{right:0;top:272px;font-family:var(--label);font-size:34px;color:var(--blue);letter-spacing:.5px}
.product-price small{font-size:22px}
.product-desc{left:0;top:312px;width:210px;font-size:13.5px;line-height:16px;color:var(--text)}
.add-cart{left:169px;top:343px;width:98px;height:37px;line-height:39px;font-size:18px;border-radius:8px}
.view-more{left:0;top:1312px;width:1200px;text-align:center;font-family:var(--label);font-size:24px;color:var(--blue);letter-spacing:.5px}

/* footer */
.site-footer{left:0;top:2176px;width:1200px;height:252px;background:var(--blue);color:var(--white)}
.footer-brand{left:0;top:30px;width:1200px;display:flex;justify-content:center;align-items:center;gap:10px;font-weight:800;font-size:28px;color:var(--white);letter-spacing:1px}
.footer-col{top:106px;width:260px;text-align:center;font-size:17px}
.footer-col h3{font-size:17px;font-weight:700;margin-bottom:8px}
.footer-col a{display:block;line-height:32px}
.bottom-bar{left:0;top:2428px;width:1200px;height:98px;background:var(--black)}
.bottom-nav{left:0;top:30px;width:1200px;display:flex;justify-content:center;gap:34px;font-family:var(--label);font-size:17px;color:#aaa;letter-spacing:.5px}
.social{left:543px;top:62px;display:flex;gap:20px}
.social span{width:22px;height:22px;border-radius:50%;background:var(--blue)}
</style>
</head>
<body>

<header class="abs site-header">
  <div class="abs brand"><span class="brand-dot"></span>MARKEN TOBLER</div>
  <nav class="abs account-nav">
    <a class="active">Home</a><a>Mein Benutzerkonto</a><a>Mein Wunschzettel</a><a>Mein Warenkorb</a><a>Zur Kasse</a><a>Anmelden</a>
  </nav>
  <div class="abs nav-caret"></div>
</header>

<section class="abs hero">
  <div class="abs coin-decor" role="img" aria-label="Dunkle Goldmünzen als Hintergrundbild"></div>
  <div class="abs stamp-art" role="img" aria-label="Alte Briefmarke in Blau und Rot, Nahaufnahme"></div>
  <nav class="abs category-nav">
    <a class="current">Briefmarken</a><a>Tobler-Alben &amp; Zubehör</a><a>Münzen &amp; Banknoten</a><a>Fehllisten-Service</a><a>Frankierservice</a><a>Ankäufe</a>
  </nav>
  <h1 class="abs hero-title">Heading in Language<br>of your choice</h1>
  <p class="abs hero-sub">Something about product</p>
  <p class="abs hero-copy">Lorem ipsum dolor sit amet, misar consectetur adipiscing elit. In viverrase felis eget gravida. Nullam enim leo.</p>
  <a class="abs btn shop-now">Shop Now</a>
</section>

<div class="abs divider-line" style="top:546px"></div>
<div class="abs divider-pill" style="left:491px;top:529px;width:214px">Gruezi Miteinander</div>

<p class="abs welcome">und ein herzliches Willkommen bei der Marken Tobler AG. Aus der bereits 1931 durch Paul Tobler gegründeten Firma, entwickelte sich in den letzten 89 Jahren eines der grössten und bekanntesten Schweizer Briefmarkenhäuser. Tobler - Qualität, das heisst Spitzenqualität ohne Wenn und Aber! Bitte überzeugen Sie sich selbst!<br>Wir freuen uns!</p>

<section class="abs products">
  <div class="abs product" style="left:171px;top:49px"><div class="abs product-image"><div class="abs coin" role="img" aria-label="Produktfoto einer Goldmünze"></div></div><div class="abs product-name">Product #1</div><div class="abs product-price"><small>$</small>125.50</div><p class="abs product-desc">Brief description of product and it’s use or properties.</p><a class="abs btn add-cart">Add to Cart</a></div>
  <div class="abs product" style="left:463px;top:49px"><div class="abs product-image"><div class="abs coin" role="img" aria-label="Produktfoto einer Goldmünze"></div></div><div class="abs product-name">Product #2</div><div class="abs product-price"><small>$</small>125.50</div><p class="abs product-desc">Brief description of product and it’s use or properties.</p><a class="abs btn add-cart">Add to Cart</a></div>
  <div class="abs product" style="left:754px;top:49px"><div class="abs product-image"><div class="abs coin" role="img" aria-label="Produktfoto einer Goldmünze"></div></div><div class="abs product-name">Product #3</div><div class="abs product-price"><small>$</small>125.50</div><p class="abs product-desc">Brief description of product and it’s use or properties.</p><a class="abs btn add-cart">Add to Cart</a></div>

  <div class="abs product" style="left:171px;top:457px"><div class="abs product-image"><div class="abs coin" role="img" aria-label="Produktfoto einer Goldmünze"></div></div><div class="abs product-name">Product #4</div><div class="abs product-price"><small>$</small>125.50</div><p class="abs product-desc">Brief description of product and it’s use or properties.</p><a class="abs btn add-cart">Add to Cart</a></div>
  <div class="abs product" style="left:463px;top:457px"><div class="abs product-image"><div class="abs coin" role="img" aria-label="Produktfoto einer Goldmünze"></div></div><div class="abs product-name">Product #5</div><div class="abs product-price"><small>$</small>125.50</div><p class="abs product-desc">Brief description of product and it’s use or properties.</p><a class="abs btn add-cart">Add to Cart</a></div>
  <div class="abs product" style="left:754px;top:457px"><div class="abs product-image"><div class="abs coin" role="img" aria-label="Produktfoto einer Goldmünze"></div></div><div class="abs product-name">Product #6</div><div class="abs product-price"><small>$</small>125.50</div><p class="abs product-desc">Brief description of product and it’s use or properties.</p><a class="abs btn add-cart">Add to Cart</a></div>

  <div class="abs product" style="left:171px;top:865px"><div class="abs product-image"><div class="abs coin" role="img" aria-label="Produktfoto einer Goldmünze"></div></div><div class="abs product-name">Product #7</div><div class="abs product-price"><small>$</small>125.50</div><p class="abs product-desc">Brief description of product and it’s use or properties.</p><a class="abs btn add-cart">Add to Cart</a></div>
  <div class="abs product" style="left:463px;top:865px"><div class="abs product-image"><div class="abs coin" role="img" aria-label="Produktfoto einer Goldmünze"></div></div><div class="abs product-name">Product #8</div><div class="abs product-price"><small>$</small>125.50</div><p class="abs product-desc">Brief description of product and it’s use or properties.</p><a class="abs btn add-cart">Add to Cart</a></div>
  <div class="abs product" style="left:754px;top:865px"><div class="abs product-image"><div class="abs coin" role="img" aria-label="Produktfoto einer Goldmünze"></div></div><div class="abs product-name">Product #9</div><div class="abs product-price"><small>$</small>125.50</div><p class="abs product-desc">Brief description of product and it’s use or properties.</p><a class="abs btn add-cart">Add to Cart</a></div>

  <a class="abs view-more">View More Products</a>
</section>

<div class="abs divider-line" style="top:818px"></div>
<div class="abs divider-pill" style="left:507px;top:802px;width:182px">Products</div>

<footer class="abs site-footer">
  <div class="abs footer-brand"><span class="brand-dot"></span>MARKEN TOBLER</div>
  <div class="abs footer-col" style="left:192px"><h3>KUNDENSERVICE</h3><a>Vertrauensgarantie</a><a>Versand</a></div>
  <div class="abs footer-col" style="left:470px"><h3>KONTAKT</h3><a>Kontakt</a><a>Impressum</a></div>
  <div class="abs footer-col" style="left:747px"><h3>INFORMATION</h3><a>AGB</a><a>Widerruf</a><a>Danteschutz</a></div>
</footer>

<div class="abs bottom-bar">
  <nav class="abs bottom-nav"><a>Mein Benutzerkonto</a><a>Mein Wunschzettel</a><a>Mein Warenkorb</a><a>Zur Kasse</a><a>Anmelden</a></nav>
  <div class="abs social"><span></span><span></span><span></span></div>
</div>

</body>
</html>
```